Silver Heron Construction Services

Create a business card for my business consulting company
Danielle Vesk, Founder and CEO
4816 Alder Brook Way, Ste 100
Denver, CO. 80451
303.782.4190 cell
dvesk@silverheronconst.example
www.silverheronconst.example

Target Market(s)

Private Equity and Construction Companies

Industry/Entity Type

Business / Sales Consulting

Contact Information for Business Card

Tag Line that says "Where The Road To Success Is Always Under Construction"

Requirements
Must have
• Logo on both sides of the card.
Nice to have
• Add tagline to the same side of the card as my name and contact info

```html
<!DOCTYPE html>
<html lang="en">
<head>
<meta charset="utf-8">
<title>Silver Heron Construction Services – Business Card</title>
<link href="https://fonts.googleapis.com/css2?family=Montserrat:wght@400;700&display=swap" rel="stylesheet">
<style>
  :root {
    --bg: #6a6a6a;
    --card: #ffffff;
    --ink: #111111;
    --muted: #2a2a2a;
  }
  * { box-sizing: border-box; margin: 0; padding: 0; }
  html, body { width: 1200px; height: 801px; overflow: hidden; }
  body {
    background: var(--bg);
    font-family: "Montserrat", sans-serif;
    color: var(--ink);
    display: flex;
    align-items: center;
    justify-content: center;
    gap: 48px;
  }
  .card {
    position: relative;
    width: 540px;
    height: 310px;
    background: var(--card);
    border-radius: 18px;
    overflow: hidden;
  }
  .card-front .accent-tab {
    position: absolute;
    top: 26px;
    right: 0;
    width: 10px;
    height: 52px;
    background: var(--ink);
  }
  .card-front .identity {
    position: absolute;
    top: 26px;
    right: 26px;
    text-align: right;
  }
  .identity .person-name {
    font-weight: 700;
    font-size: 24px;
    letter-spacing: 0.2px;
  }
  .identity .person-title {
    font-size: 14px;
    color: var(--muted);
    margin-top: 2px;
  }
  .card-front .brand-lockup {
    position: absolute;
    left: 28px;
    top: 110px;
    width: 170px;
    display: flex;
    align-items: center;
    gap: 8px;
    font-weight: 700;
    font-size: 15px;
    line-height: 1.15;
    text-transform: uppercase;
  }
  .brand-mark {
    flex: none;
    width: 14px;
    height: 14px;
    background: var(--ink);
  }
  .card-front .details {
    position: absolute;
    left: 218px;
    top: 104px;
    font-size: 13px;
    line-height: 1.45;
    color: var(--muted);
  }
  .details .tagline { font-size: 14.5px; margin-bottom: 16px; }
  .details .address { margin-bottom: 14px; }
  .details .contact-line {
    display: flex;
    align-items: center;
    gap: 6px;
  }
  .details .contact-line svg { width: 13px; height: 13px; fill: var(--ink); }
  .card-back {
    display: flex;
    align-items: center;
    justify-content: center;
  }
  .card-back .brand-lockup {
    display: flex;
    align-items: center;
    gap: 14px;
    font-weight: 700;
    font-size: 26px;
    line-height: 1.15;
    text-transform: uppercase;
    text-align: left;
  }
  .card-back .brand-mark { width: 22px; height: 22px; }
</style>
</head>
<body>
  <section class="card card-front" aria-label="Business card front">
    <div class="accent-tab"></div>
    <div class="identity">
      <div class="person-name">Danielle Vesk</div>
      <div class="person-title">Founder and CEO</div>
    </div>
    <div class="brand-lockup">
      <span class="brand-mark"></span>
      <span>Silver Heron Construction Services</span>
    </div>
    <div class="details">
      <p class="tagline">The Road To Success Is Always Under Construction</p>
      <p class="address">4816 Alder Brook Way,<br>Ste 100 Denver, CO. 80451</p>
      <p class="contact-line">
        <svg viewBox="0 0 24 24" aria-hidden="true"><path d="M6.6 10.8a15.1 15.1 0 0 0 6.6 6.6l2.2-2.2a1 1 0 0 1 1-.25 11.4 11.4 0 0 0 3.6.57 1 1 0 0 1 1 1V20a1 1 0 0 1-1 1A17 17 0 0 1 3 4a1 1 0 0 1 1-1h3.5a1 1 0 0 1 1 1c0 1.25.2 2.45.57 3.57a1 1 0 0 1-.25 1z"/></svg>
        303.782.4190
      </p>
      <p class="contact-line">
        <svg viewBox="0 0 24 24" aria-hidden="true"><path d="M3 5h18a1 1 0 0 1 1 1v12a1 1 0 0 1-1 1H3a1 1 0 0 1-1-1V6a1 1 0 0 1 1-1zm9 7.2L4.5 7v.4L12 13l7.5-5.6V7z"/></svg>
        dvesk@silverheronconst.example
      </p>
    </div>
  </section>

  <section class="card card-back" aria-label="Business card back">
    <div class="brand-lockup">
      <span class="brand-mark"></span>
      <span>Silver Heron<br>Construction Services</span>
    </div>
  </section>
</body>
</html>
```